Webdesign Tischlerei Wallbusch
Zielgruppe
es handelt sich um eine Tischlerei / Meisterbetrieb
Zielgruppe: private und gwerbliche Kunden
Aufgabenstellung
- die Vielfältigkeit der Produkte aus eigener Herstellung durch Meisterhand soll vermittelt werden
- FixWerk Systemspezialist
- Produktschulungen Kork
- KEINE Kopie der alten Seite
- aufgelockert und modern
- gern mit Elementen in leichter Holzoptik und weichen Rundungen
- Farben modern und in Telen an das Logo angepasst
Vorstellung des Kunden zur Navigationsstruktur:
Navigationsstruktur Website
1. wo arbeiten wir... (in der Werkstatt findet mittlerweile der geringere Anteil der Arbeit statt)
• Bild Werkstatt von außen/Schild
• Mitarbeiter an der Säge
• und/oder Mitarbeiter an der Hobelmaschine
• Gespräch/Planung/Skizzen
• evtl. (gepacktes) Fahrzeug(denn das ist ein wichtiges Arbeitsmittel)
2. was macht uns aus...
• vernünftiges Verhältnis zu den Mitarbeitern, ermöglicht eine kontinuierliche, fachgerechte und qualitativ hochwertige Arbeit an den Projekten
• überwiegend handwerkliche Fertigung
• Verwendung von Materialien und Hölzern- auch aus der Region
• Flexibilität im Umgang mit Arbeitszeit, Material und Leistungen
3. welche Möglichkeiten haben wir....
• „Liste“ mit den Möglichkeiten die wir so haben(z.B. Herstellung und Reparaturen von individuellen Treppen, Möbeln, Türen, Lieferung und Reparatur von Fenstern, verlegen und reparieren von Fußböden wie Hobeldielen, Parkett, Designböden, Carport, Zäune, Tore
• Galerie Projekte mit Beschreibung
• vorher-nachher Bilder mit Beschreibung
4. was sollte Sie interessieren...
• Tipps &Tricks rund ums Holz/Produkte(Fenster Pflegehinweise)
• Termine und Veranstaltungen auch nicht betrieblich
• Empfehlungen (Produkte, Materialien, Pflegemittel -was wir benutzen und gefällt oder ist das dann Werbung?)
5. womit könnten wir ihnen helfen...
• Interaktives Anfrageformular
• Möglichkeit Skizzen hochzuladen, Wünsche zu beschreiben
6. wie erreichen Sie uns...<..

```html
<!DOCTYPE html>
<html lang="de">
<head>
<meta charset="utf-8">
<title>Menü</title>
<link rel="stylesheet" href="https://fonts.googleapis.com/css2?family=Work+Sans:wght@400&display=swap">
<style>
  :root {
    --brand-blue: #0a69a6;
    --menu-text: #ffffff;
    --menu-active: #f2a93b;
  }
  * { margin: 0; padding: 0; box-sizing: border-box; }
  html, body {
    width: 1200px;
    height: 675px;
    overflow: hidden;
  }
  body {
    background: var(--brand-blue);
    font-family: "Work Sans", Arial, sans-serif;
    position: relative;
  }
  .menu-close {
    position: absolute;
    left: 1141px;
    top: 26px;
    width: 23px;
    height: 23px;
    display: block;
  }
  .main-nav {
    position: absolute;
    left: 331px;
    top: 128px;
  }
  .main-nav ul { list-style: none; }
  .main-nav a {
    display: block;
    font-size: 32px;
    line-height: 59px;
    font-weight: 400;
    letter-spacing: 0.02em;
    color: var(--menu-text);
    text-decoration: none;
    white-space: nowrap;
  }
  .main-nav a.is-active { color: var(--menu-active); }
</style>
</head>
<body>
  <svg class="menu-close" viewBox="0 0 23 23" aria-label="Menü schließen" role="img">
    <path d="M1 1 L22 22 M22 1 L1 22" stroke="#ffffff" stroke-width="2" stroke-linecap="square" fill="none"/>
  </svg>
  <nav class="main-nav" aria-label="Hauptnavigation">
    <ul>
      <li><a class="is-active" href="#">Startseite</a></li>
      <li><a href="#">Wo arbeiten wir?</a></li>
      <li><a href="#">Was macht uns aus?</a></li>
      <li><a href="#">Welche Möglichkeiten haben wir?</a></li>
      <li><a href="#">Was sollte Sie interessieren?</a></li>
      <li><a href="#">Womit könnten wir ihnen helfen?</a></li>
      <li><a href="#">Wie erreichen Sie uns?</a></li>
    </ul>
  </nav>
</body>
</html>
```